Labels for fruit liqueur bottles

We are looking for a visual identity based on our logo, for fruit liqueur labels. To date, we have different liqueurs such as: lemon liqueur, orange liqueurs, mandarin liqueurs, grapefruit liqueurs. We will then create other liqueurs such as strawberry, apple or even apricot. Our goal is to have a single visual that we can adapt in different colors depending on the fruit used.

On the label there should be:
the logo
homemade
the name of the fruit (which can be changed depending on the product)
swiss-made
50cl
21°

Colors

Designer to choose colors to be used in the design.

Requirements
Must have
• a visual of liquor bottle labels, with the possibility of changing the background colors, depending on the fruit used
Nice to have
• something modern and nice to look at. We must be able to read the basic fruit in the blink of an eye. it is also possible to have a black or white or colored label background.

```html
<!DOCTYPE html>
<html lang="fr">
<head>
<meta charset="utf-8">
<title>Casa Velmora – liqueurs de fruits</title>
<link href="https://fonts.googleapis.com/css2?family=Oswald:wght@400;600;700&display=swap" rel="stylesheet">
<style>
  :root {
    --backdrop: #e8c3ae;
    --white: #ffffff;
    --ink: #e8501a;
    --footer: #ee5a14;
    --stripe-green: #9cc43a;
    --stripe-yellow: #f4c81e;
    --stripe-orange: #f47a1e;
  }
  * { margin: 0; padding: 0; box-sizing: border-box; }
  html, body { width: 1200px; height: 800px; overflow: hidden; }
  body {
    background: var(--backdrop);
    font-family: 'Oswald', sans-serif;
    display: flex;
    align-items: center;
    justify-content: center;
  }
  .label-range { display: flex; gap: 30px; }
  .label {
    width: 160px;
    height: 272px;
    border: 3px solid var(--white);
    display: flex;
    flex-direction: column;
    background: var(--tone-low);
  }
  .label__field {
    flex: 1;
    position: relative;
    background: linear-gradient(to bottom, var(--tone-high) 0 36%, var(--tone-low) 36% 100%);
    display: flex;
    justify-content: center;
    padding-top: 48px;
  }
  .label__panel {
    width: 88px;
    height: 92px;
    background: var(--white);
    border: 1px solid var(--ink);
    display: flex;
    flex-direction: column;
    align-items: center;
    padding-top: 6px;
    color: var(--ink);
    text-align: center;
  }
  .label__mark {
    width: 11px; height: 11px;
    border-radius: 50%;
    background: var(--ink);
  }
  .label__kind { font-size: 7px; font-weight: 600; margin-top: 7px; line-height: 1; }
  .label__fruit { font-size: 12px; font-weight: 700; line-height: 1.2; letter-spacing: 0.2px; }
  .label__brand { font-size: 6.5px; font-weight: 600; margin-top: auto; margin-bottom: 6px; }
  .label__stripes { display: flex; flex-direction: column; }
  .label__stripes span { display: block; height: 3px; }
  .label__stripes .s1 { background: var(--stripe-green); }
  .label__stripes .s2 { background: var(--stripe-yellow); height: 2px; }
  .label__stripes .s3 { background: var(--stripe-orange); }
  .label__stripes .s4 { background: var(--white); height: 2px; }
  .label__footer {
    background: var(--footer);
    color: var(--white);
    height: 40px;
    display: flex;
    flex-direction: column;
    align-items: center;
    justify-content: center;
    gap: 3px;
  }
  .label__craft { font-size: 6.5px; font-weight: 600; letter-spacing: 0.3px; }
  .label__facts { font-size: 5.5px; display: flex; gap: 5px; }
  .label__facts span + span { border-left: 1px solid var(--white); padding-left: 5px; }

  .label--citron    { --tone-high: #d6ea4c; --tone-low: #ece82e; }
  .label--noix      { --tone-high: #5a2810; --tone-low: #7a3712; }
  .label--grapefruit{ --tone-high: #f2788c; --tone-low: #f68ea2; }
  .label--mandarin  { --tone-high: #f5891e; --tone-low: #f8a052; }
  .label--fraise    { --tone-high: #de2e3a; --tone-low: #e8464e; }
  .label--orange    { --tone-high: #f0662a; --tone-low: #f7834f; }
</style>
</head>
<body>
  <main class="label-range">
    <article class="label label--citron">
      <div class="label__field"><div class="label__panel"><span class="label__mark"></span><p class="label__kind">liqueur de</p><h2 class="label__fruit">CITRON</h2><p class="label__brand">CASA VELMORA</p></div></div>
      <div class="label__stripes"><span class="s1"></span><span class="s2"></span><span class="s3"></span><span class="s4"></span></div>
      <footer class="label__footer"><p class="label__craft">fabrication artisanale</p><p class="label__facts"><span>swiss made</span><span>21% vol</span><span>500ml</span></p></footer>
    </article>
    <article class="label label--noix">
      <div class="label__field"><div class="label__panel"><span class="label__mark"></span><p class="label__kind">liqueur de</p><h2 class="label__fruit">NOIX</h2><p class="label__brand">CASA VELMORA</p></div></div>
      <div class="label__stripes"><span class="s1"></span><span class="s2"></span><span class="s3"></span><span class="s4"></span></div>
      <footer class="label__footer"><p class="label__craft">fabrication artisanale</p><p class="label__facts"><span>swiss made</span><span>21% vol</span><span>500ml</span></p></footer>
    </article>
    <article class="label label--grapefruit">
      <div class="label__field"><div class="label__panel"><span class="label__mark"></span><p class="label__kind">liqueur de</p><h2 class="label__fruit">GRAPPEFRUITS</h2><p class="label__brand">CASA VELMORA</p></div></div>
      <div class="label__stripes"><span class="s1"></span><span class="s2"></span><span class="s3"></span><span class="s4"></span></div>
      <footer class="label__footer"><p class="label__craft">fabrication artisanale</p><p class="label__facts"><span>swiss made</span><span>21% vol</span><span>500ml</span></p></footer>
    </article>
    <article class="label label--mandarin">
      <div class="label__field"><div class="label__panel"><span class="label__mark"></span><p class="label__kind">liqueur de</p><h2 class="label__fruit">MANDARIN</h2><p class="label__brand">CASA VELMORA</p></div></div>
      <div class="label__stripes"><span class="s1"></span><span class="s2"></span><span class="s3"></span><span class="s4"></span></div>
      <footer class="label__footer"><p class="label__craft">fabrication artisanale</p><p class="label__facts"><span>swiss made</span><span>21% vol</span><span>500ml</span></p></footer>
    </article>
    <article class="label label--fraise">
      <div class="label__field"><div class="label__panel"><span class="label__mark"></span><p class="label__kind">liqueur de</p><h2 class="label__fruit">FRAISE</h2><p class="label__brand">CASA VELMORA</p></div></div>
      <div class="label__stripes"><span class="s1"></span><span class="s2"></span><span class="s3"></span><span class="s4"></span></div>
      <footer class="label__footer"><p class="label__craft">fabrication artisanale</p><p class="label__facts"><span>swiss made</span><span>21% vol</span><span>500ml</span></p></footer>
    </article>
    <article class="label label--orange">
      <div class="label__field"><div class="label__panel"><span class="label__mark"></span><p class="label__kind">liqueur d'</p><h2 class="label__fruit">ORANGE</h2><p class="label__brand">CASA VELMORA</p></div></div>
      <div class="label__stripes"><span class="s1"></span><span class="s2"></span><span class="s3"></span><span class="s4"></span></div>
      <footer class="label__footer"><p class="label__craft">fabrication artisanale</p><p class="label__facts"><span>swiss made</span><span>21% vol</span><span>500ml</span></p></footer>
    </article>
  </main>
</body>
</html>
```